Business card design for upmarket Home Technology design and Installation company

Hello designers, we need a great business card designed.
We need it to convey high tech, and also sophistication .
We work with some of the most affluent people in the world building them home technology systems, and A/V entertainment systems.

Services offered include the following:
Design, sales, installation, and maintenance of

*Home Automation systems
*Distributed / Multi-Room Audio and Video
*High Performance Networks & WiFi
* Lighting and Shade Control
*Home cinema
*Security and CCTV Systems

I have included a copy of our logo to use for your design efforts.

Target Market(s)

Upmarket clients with multi million euro villas.

Industry/Entity Type

Home technology

Contact Information for Business Card

NAME: Derek Halloran ADDRESS: Plaza Brisa Local 42, Port Serella, 07392 PHONE: +34-602-518-794 EMAIL: DHalloran@VELTRAsmarthomes.com WEB: www.veltrasmarthomes.com

Requirements
Must have
• Our Logo, and our tagline

```html
<!DOCTYPE html>
<html lang="en">
<head>
<meta charset="utf-8">
<title>VELTRA Business Card</title>
<link rel="stylesheet" href="https://fonts.googleapis.com/css2?family=Source+Sans+3:wght@400;600;700&display=swap">
<style>
  :root {
    --bg: #e9e6e1;
    --card: #1a1a1a;
    --gold: #c9a552;
    --gold-light: #e6c87a;
    --gold-dark: #a8843a;
    --text: #ececec;
    --muted: #bdbdbd;
    --rule: #444;
  }
  * { box-sizing: border-box; margin: 0; padding: 0; }
  html, body { width: 1200px; height: 801px; overflow: hidden; }
  body {
    background: var(--bg);
    font-family: "Source Sans 3", sans-serif;
    display: flex; align-items: center; justify-content: center; gap: 40px;
  }
  .card {
    position: relative;
    width: 540px; height: 310px;
    background: var(--card);
    border-radius: 18px;
    overflow: hidden;
    box-shadow: 0 10px 30px rgba(0,0,0,.25);
    color: var(--text);
  }
  /* Front */
  .brand {
    position: absolute; left: 48px; top: 92px; width: 190px;
    display: flex; flex-direction: column; align-items: center;
  }
  .brand-dot {
    width: 70px; height: 70px; border-radius: 50%;
    background: linear-gradient(135deg, var(--gold-light), var(--gold-dark));
    margin-bottom: 16px;
  }
  .brand-name {
    font-size: 38px; font-weight: 600; letter-spacing: 4px; color: var(--gold);
    line-height: 1;
  }
  .brand-tagline {
    margin-top: 6px; font-size: 11px; letter-spacing: 4px; color: var(--gold);
  }
  .services {
    position: absolute; left: 250px; top: 72px; width: 275px;
    list-style: none; font-size: 12.5px; line-height: 1.55; color: var(--muted);
  }
  .services li { position: relative; padding-left: 16px; white-space: nowrap; }
  .services li::before {
    content: ""; position: absolute; left: 0; top: 7px;
    width: 6px; height: 6px; border-radius: 50%; border: 1.5px solid var(--gold);
  }
  /* Back */
  .person { position: absolute; left: 14px; top: 100px; width: 234px; text-align: right; }
  .person-name { font-size: 25px; font-weight: 600; color: var(--text); letter-spacing: .5px; line-height: 1; white-space: nowrap; }
  .person-title { font-size: 15px; color: var(--gold); margin-top: 4px; }
  .divider { position: absolute; left: 260px; top: 70px; width: 1px; height: 100px; background: var(--rule); }
  .contact { position: absolute; left: 276px; top: 68px; list-style: none; font-size: 12.5px; color: var(--muted); line-height: 1.45; }
  .contact li { display: flex; gap: 8px; align-items: flex-start; white-space: nowrap; }
  .contact svg { flex: none; width: 11px; height: 11px; margin-top: 3px; fill: var(--gold); }
  .contact .phone { font-weight: 700; color: var(--text); }
  .band {
    position: absolute; left: 0; right: 0; top: 232px; height: 34px;
    background: linear-gradient(90deg, var(--gold-dark), var(--gold-light));
    display: flex; align-items: center; justify-content: center;
    font-size: 13px; letter-spacing: 3px; color: #1a1a1a;
  }
  .band strong { font-weight: 700; }
  .band-dot {
    position: absolute; right: 40px; top: 6px;
    width: 22px; height: 22px; border-radius: 50%; background: var(--card);
  }
</style>
</head>
<body>
  <section class="card card-front">
    <div class="brand">
      <div class="brand-dot"></div>
      <div class="brand-name">VELTRA</div>
      <div class="brand-tagline">LUXURY LIVING</div>
    </div>
    <ul class="services">
      <li>Design, sales, installation, &amp; maintenance of</li>
      <li>Home Automation Systems</li>
      <li>Distributed / Multi-Room Audio &amp; Video</li>
      <li>High Performance Networks &amp; WiFi</li>
      <li>Lighting &amp; Shade Control</li>
      <li>Home Cinema</li>
      <li>Security &amp; CCTV Systems</li>
    </ul>
  </section>

  <section class="card card-back">
    <div class="person">
      <div class="person-name">DEREK HALLORAN</div>
      <div class="person-title">Managing Director</div>
    </div>
    <div class="divider"></div>
    <ul class="contact">
      <li>
        <svg viewBox="0 0 12 12" aria-hidden="true"><path d="M6 0a4 4 0 0 0-4 4c0 3 4 8 4 8s4-5 4-8a4 4 0 0 0-4-4zm0 5.5A1.5 1.5 0 1 1 6 2.5a1.5 1.5 0 0 1 0 3z"/></svg>
        <span>Plaza Brisa Local 42<br>Port Serella 07392</span>
      </li>
      <li>
        <svg viewBox="0 0 12 12" aria-hidden="true"><path d="M2.5 0.5l2 2.5-1.2 1.2a7 7 0 0 0 4.5 4.5L9 7.5l2.5 2-1.3 2C5 11.5.5 7 .5 1.8z"/></svg>
        <span class="phone">+34-602-518-794</span>
      </li>
      <li>
        <svg viewBox="0 0 12 12" aria-hidden="true"><path d="M0 2h12v8H0zM1 3l5 4 5-4z"/></svg>
        <span>DHalloran@VELTRAsmarthomes.com</span>
      </li>
    </ul>
    <div class="band"><strong>VELTRA</strong>SMARTHOMES.COM<span class="band-dot"></span></div>
  </section>
</body>
</html>
```